Einladungskarten-Design für Schützenverein
super gute Zusammenarbeit. Werde für weitere Arbeiten gerne darauf zurückkommen.
Zielgruppe
Wir sind ein Schützenverein und möchten mit einem neuzeitlichen Design für unser traditionelles Grümpelschiessen Werbung machen und die jüngere Generation für diesen schönen Sport begeistern.

```html
<!DOCTYPE html>
<html lang="de">
<head>
<meta charset="utf-8">
<title>Einladung zum Grümpelschiessen 2021</title>
<link rel="stylesheet" href="https://fonts.googleapis.com/css2?family=Montserrat:wght@800&family=Lato:wght@400;700;900&display=swap">
<style>
  :root {
    --navy: #1f2a7a;
    --yellow: #f0c800;
    --white: #ffffff;
    --panel: #f4f5f8;
    --grass-light: #8fbf3a;
    --grass-dark: #3f7a1e;
    --forest-light: #c9c24a;
    --forest-dark: #5b6a2c;
    --backdrop: #e6e6e6;
  }
  * { box-sizing: border-box; margin: 0; padding: 0; }
  html, body { width: 1200px; height: 800px; overflow: hidden; }
  body { background: var(--backdrop); font-family: "Lato", sans-serif; }

  .flyer {
    position: absolute; left: 340px; top: 30px;
    width: 520px; height: 740px; overflow: hidden;
    background: linear-gradient(180deg, var(--grass-light), var(--grass-dark));
    box-shadow: 0 10px 30px rgba(0,0,0,.25);
  }
  .hero-photo {
    position: absolute; left: 0; top: 0; width: 520px; height: 380px;
    background: linear-gradient(160deg, var(--forest-dark) 0%, #8b9a3c 45%, var(--forest-light) 75%, var(--grass-light) 100%);
  }

  .club-mark {
    position: absolute; right: 30px; top: 40px; width: 120px; height: 120px;
    background: var(--white); padding: 14px 10px;
    display: flex; flex-direction: column; align-items: center; justify-content: center; gap: 10px;
  }
  .club-mark .dot { width: 22px; height: 22px; background: var(--yellow); }
  .club-mark .name {
    color: var(--navy); font-weight: 900; font-size: 13px; line-height: 1.2;
    text-align: center; text-transform: uppercase;
  }

  .info-panel {
    position: absolute; left: 40px; top: 282px; width: 430px; height: 400px;
    background: var(--panel); border-radius: 24px;
  }

  .title-band {
    position: absolute; font-family: "Montserrat", sans-serif; font-weight: 800;
    color: var(--white); text-transform: uppercase; text-align: center; white-space: nowrap;
  }
  .title-band.intro { left: 100px; top: 220px; width: 300px; height: 42px; background: var(--yellow); font-size: 28px; line-height: 42px; }
  .title-band.event { left: 55px; top: 262px; width: 420px; height: 48px; background: var(--navy); font-size: 34px; line-height: 48px; }
  .title-band.year  { left: 190px; top: 310px; width: 140px; height: 56px; background: var(--yellow); font-size: 48px; line-height: 56px; }

  .date-block {
    position: absolute; left: 52px; top: 380px; width: 156px;
    text-align: right; color: var(--navy); font-weight: 700;
  }
  .date-block .day { font-size: 36px; font-weight: 900; line-height: 1; }
  .date-block .date { font-size: 18px; margin-top: 4px; }
  .date-block .time { font-size: 18px; margin-top: 8px; line-height: 1.15; }

  .divider { position: absolute; left: 214px; top: 380px; width: 3px; height: 225px; background: var(--navy); }

  .details { position: absolute; left: 226px; top: 380px; width: 222px; color: var(--navy); font-size: 12.5px; line-height: 1.28; }
  .details dt { font-weight: 900; font-size: 14px; margin-top: 6px; }
  .details dt:first-child { margin-top: 0; }

  .shooter-art {
    position: absolute; left: 40px; top: 560px; width: 160px; height: 60px;
    background: var(--navy); border-radius: 40px 40px 0 0;
  }
  .scope-post { position: absolute; left: 455px; top: 585px; width: 8px; height: 40px; background: var(--navy); border-radius: 4px; }

  .footer-band { position: absolute; left: 0; top: 620px; width: 520px; height: 120px; }
  .footer-text {
    position: absolute; left: 30px; top: 636px; width: 460px;
    color: var(--white); font-weight: 900; font-size: 15px; line-height: 1.35; text-align: center;
  }
  .footer-url {
    position: absolute; left: 120px; top: 703px; width: 220px;
    color: var(--navy); font-weight: 900; font-size: 17px; text-align: center;
  }
</style>
</head>
<body>
  <article class="flyer">
    <div class="hero-photo" role="img" aria-label="Foto: junge Schützin liegt mit Gewehr im Gras am Waldrand"></div>

    <div class="club-mark">
      <span class="dot"></span>
      <span class="name">Schützenverein Talbach</span>
    </div>

    <div class="info-panel"></div>

    <h1>
      <span class="title-band intro">Einladung zum</span>
      <span class="title-band event">Grümpelschiessen</span>
      <span class="title-band year">2021</span>
    </h1>

    <div class="date-block">
      <p class="day">Sonntag</p>
      <p class="date">29. August</p>
      <p class="time">08.00 - 12.00<br>Uhr durchgehend</p>
    </div>

    <div class="divider"></div>

    <dl class="details">
      <dt>Wo :</dt>
      <dd>BEIM SCHÜTZENHAUS TALBACH (Parkplätze bei der Talstation der Sonnbahn)</dd>
      <dt>Wer :</dt>
      <dd>Einzel, Paare und Familien &gt; einfach jedermann ob jung ob alt aus nah und fern, Frau und Mann</dd>
      <dt>Unser Angebot :</dt>
      <dd>Grümpelstich und Festwirtschaft mit Mittags -menü in herrlicher Umgebung</dd>
    </dl>

    <div class="shooter-art" role="img" aria-label="Silhouette zweier liegender Schützen mit Gewehren"></div>
    <div class="scope-post"></div>

    <svg class="footer-band" viewBox="0 0 520 120" aria-hidden="true">
      <rect x="0" y="0" width="520" height="100" fill="var(--navy)"/>
      <rect x="0" y="100" width="520" height="20" fill="var(--yellow)"/>
      <polygon points="110,100 128,78 332,78 350,100" fill="var(--yellow)"/>
    </svg>
    <p class="footer-text">Wir laden Sie herzlich zu einem gemütlichen Sonntag ein und freuen uns auf Ihren Besuch und Ihre Teilnahme.</p>
    <p class="footer-url">www.svtalbach.ch</p>
  </article>
</body>
</html>
```